Real Estate Investor needs awesome business card design

I invest in real estate, focused on multi-family properties, and I need a business card to hand out to potential partners. I prefer simple, clean designs, but it needs to stand out, so I'd like there to be a bit of red in the design as well.

It should include this information:

Front
Calder Whitby
Real Estate Investor
Direct phone: 501-555-0187
Email: calderjwhitby@mailbox-example.net
Headshot (Picture), I've uploaded a few, just pick the one you think looks best with your design. You can remove the background from the headshot image if it looks better.

Back
The back of the card's design should flow and be congruent with the front. On the back I want to put an inspirational quote or question. There will be different ones depending on the card, so I'll need the original file so I can edit it in the end.

For now, use “The Pessimist Sees Difficulty In Every Opportunity. The Optimist Sees The Opportunity In Every Difficulty.” -Edmund Halvorsen

Target Market(s)

Investors

Industry/Entity Type

Real Estate

Contact Information for Business Card

Front
Calder Whitby
Real Estate Investor

Back
The back of the card's design should flow and be congruent with the front. On the back I want to put an inspirational quote or question. There will be different ones depending on the card, so I'll need the original file so I can edit it in the end. I've uploaded some EXAMPLES of business cards with quotes on them. Don't copy but feel free to use them as inspiration.

The design will be printed on "ZAP sized" business cards
1039 x 697 pixels
with rounded corners

Font styles to use
Serif
Decorative
Script

Colors
ec1f27

Requirements
Must have
• Headshot, name, and other information in it.
• 1039 x 697 pixels
• Rounded corners
• Clean design that pops. I'm open to see any color background, including black.
• Headshots can be located here: https://www.filecrate-example.com/sh/8kx2vq71ld0pa3z/BQQTXL7mrrf9eT3Kq0HhgkLm2b?dl=0
Nice to have
• It would be awesome if the design included a personal signature or monogram, but if not I'll get a personal logo developed later and the card redesigned if I think it needs it.
Should not have
• Cluttered design

```html
<!DOCTYPE html>
<html lang="en">
<head>
<meta charset="utf-8">
<title>Calder Whitby – Business Card</title>
<link rel="stylesheet" href="https://fonts.googleapis.com/css2?family=Alegreya:ital,wght@0,400;0,700;1,400&display=swap">
<style>
  :root {
    --bg: #ebeae7;
    --card: #ffffff;
    --red: #e3252b;
    --ink: #141414;
    --grey: #5d5d5d;
    --white: #ffffff;
  }
  * { box-sizing: border-box; margin: 0; padding: 0; }
  html, body {
    width: 1200px;
    height: 878px;
    overflow: hidden;
    background: var(--bg);
    font-family: "Alegreya", Georgia, serif;
  }
  .canvas { position: relative; width: 1200px; height: 878px; }
  .card {
    position: absolute;
    width: 540px;
    height: 362px;
    border-radius: 20px;
    overflow: hidden;
    background: var(--card);
    box-shadow: 0 6px 18px rgba(0,0,0,0.12);
  }
  .card-back { left: 40px; top: 70px; }
  .card-front { left: 620px; top: 446px; }
  .card-wave { position: absolute; inset: 0; width: 100%; height: 100%; }
  .wave-fill { fill: var(--red); }
  .wave-edge { fill: none; stroke: var(--ink); stroke-width: 5; }

  /* back */
  .quote {
    position: absolute;
    left: 40px; right: 40px; top: 70px;
    text-align: center;
    font-style: italic;
    font-size: 21px;
    line-height: 1.75;
    color: var(--ink);
  }
  .quote-author {
    position: absolute;
    right: 52px; top: 168px;
    font-size: 13px;
    color: var(--grey);
    letter-spacing: 0.3px;
  }

  /* front */
  .headshot {
    position: absolute;
    left: 58px; top: 44px;
    width: 150px; height: 150px;
    border-radius: 50%;
    background: radial-gradient(circle at 50% 55%, #b98d78 0%, #6a4e45 30%, #1d2433 55%, #000 72%);
  }
  .identity {
    position: absolute;
    left: 250px; top: 84px;
  }
  .name {
    font-weight: 700;
    font-size: 36px;
    line-height: 1;
    color: var(--ink);
  }
  .name-first { color: var(--red); }
  .role {
    margin-top: 8px;
    margin-left: 30px;
    font-style: italic;
    font-size: 19px;
    color: var(--grey);
  }
  .contact {
    position: absolute;
    right: 42px; bottom: 34px;
    text-align: right;
    color: var(--white);
    font-size: 17px;
    line-height: 1.65;
  }
</style>
</head>
<body>
<main class="canvas">

  <section class="card card-back" aria-label="Card back">
    <svg class="card-wave" viewBox="0 0 540 362" preserveAspectRatio="none" aria-hidden="true">
      <path class="wave-fill" d="M0 248 C 150 236, 330 232, 540 205 L540 362 L0 362 Z"/>
      <path class="wave-edge" d="M0 248 C 150 236, 330 232, 540 205"/>
    </svg>
    <p class="quote">“The Pessimist Sees Difficulty In Every Opportunity.<br>The Optimist Sees The Opportunity In Every Difficulty.”</p>
    <p class="quote-author">Edmund Halvorsen</p>
  </section>

  <section class="card card-front" aria-label="Card front">
    <svg class="card-wave" viewBox="0 0 540 362" preserveAspectRatio="none" aria-hidden="true">
      <path class="wave-fill" d="M0 232 C 140 262, 320 246, 540 226 L540 362 L0 362 Z"/>
      <path class="wave-edge" d="M0 232 C 140 262, 320 246, 540 226"/>
    </svg>
    <div class="headshot" role="img" aria-label="Headshot of Calder Whitby on a black circle"></div>
    <div class="identity">
      <h1 class="name"><span class="name-first">Calder</span> Whitby</h1>
      <p class="role">Real Estate Investor</p>
    </div>
    <div class="contact">
      <p class="contact-phone">501-555-0187</p>
      <p class="contact-email">calderjwhitby@mailbox-example.net</p>
    </div>
  </section>

</main>
</body>
</html>
```